Soy Candle Business needs a label design

We need a label design for a new company selling soy candles - Velvet Hearth Studio.

We are using apothecary jars in 3 sizes.
As per attached candles will be dressed with a beautiful black bow and all finished with a diamante in centre of bow.

We would like label done on lid of candle jars - 5cm circle (5cm from one side to the other), this way one label will fit each product size. Label will be done as a sticker.

We are thinking of the background colour to be black, however are open to recommendations. We want label to be classy, elegant and simple.

Inspiration for candle design came from attached invitation that features the bow, and beautiful vintage paper on top area.

Label should include the following 3 pieces of information:
Velvet Hearth Studio (company name)
Coconut Lime (this will change depending on fragrance)
Soy Candle

Velvet Hearth Studio does not have a company logo... what is done for the label will set tone for what is done across other elements of business moving forward.

Industry/Entity Type

Business

Requirements
Must have
• Velvet Hearth Studio
Fragrance Flavour
Soy Candle

```html
<!DOCTYPE html>
<html lang="en">
<head>
<meta charset="utf-8">
<title>Velvet Hearth Studio – Lid Label Options</title>
<link rel="stylesheet" href="https://fonts.googleapis.com/css2?family=Sacramento&family=La+Belle+Aurore&family=Pinyon+Script&family=Waiting+for+the+Sunrise&display=swap">
<style>
  :root {
    --page-bg: #ffffff;
    --divider: #b9b9b9;
    --label-dark: #1f1f1f;
    --label-mid: #3a3a3a;
    --label-edge: #2a2a2a;
    --rule-line: rgba(255, 255, 255, 0.16);
    --ink-white: #f4f4f4;
    --ink-cream: #f1edc2;
    --ink-rose: #e6b7c3;
    --ink-small: #c9c9c9;
  }

  * { box-sizing: border-box; margin: 0; padding: 0; }

  html, body {
    width: 1200px;
    height: 960px;
    overflow: hidden;
    background: var(--page-bg);
  }

  .sheet {
    position: relative;
    width: 1200px;
    height: 960px;
  }

  .option-row {
    position: absolute;
    left: 0;
    width: 1200px;
    height: 260px;
  }
  .option-row--fine   { top: 56px; }
  .option-row--round  { top: 368px; }
  .option-row--formal { top: 674px; }

  .row-divider {
    position: absolute;
    left: 157px;
    width: 908px;
    height: 1px;
    background: var(--divider);
  }
  .row-divider--first  { top: 338px; }
  .row-divider--second { top: 650px; }

  .label {
    position: absolute;
    top: 8px;
    width: 244px;
    height: 244px;
    border-radius: 50%;
    overflow: hidden;
  }
  .label--white { left: 156px; --ink: var(--ink-white); }
  .label--cream { left: 482px; --ink: var(--ink-cream); }
  .label--rose  { left: 808px; --ink: var(--ink-rose); }

  .label__paper {
    position: absolute;
    inset: 0;
    border-radius: 50%;
    background: radial-gradient(circle at 50% 45%, var(--label-mid) 0%, var(--label-dark) 70%, var(--label-edge) 100%);
  }

  .label__rule {
    position: absolute;
    left: 0;
    right: 0;
    top: 158px;
    height: 1px;
    background: var(--rule-line);
  }

  .label__name {
    position: absolute;
    left: 0;
    right: 0;
    text-align: center;
    white-space: nowrap;
    color: var(--ink);
  }

  .option-row--fine .label__name {
    font-family: "Sacramento", cursive;
    font-size: 32px;
    line-height: 40px;
    top: 50px;
  }
  .option-row--round .label__name {
    font-family: "La Belle Aurore", cursive;
    font-size: 27px;
    line-height: 40px;
    letter-spacing: 0.5px;
    top: 50px;
  }
  .option-row--formal .label__name {
    font-family: "Pinyon Script", cursive;
    font-size: 33px;
    line-height: 42px;
    top: 46px;
    text-shadow: 1px 2px 2px rgba(0, 0, 0, 0.7);
  }

  .label__fragrance {
    position: absolute;
    left: 0;
    right: 0;
    top: 172px;
    text-align: center;
    white-space: nowrap;
    font-family: "Waiting for the Sunrise", cursive;
    font-size: 15px;
    line-height: 24px;
    color: var(--ink-small);
  }
</style>
</head>
<body>
<main class="sheet">

  <section class="option-row option-row--fine">
    <div class="label label--white">
      <div class="label__paper" role="img" aria-label="Dark charcoal vintage damask paper background"></div>
      <div class="label__rule"></div>
      <p class="label__name">Velvet Hearth<br>Studio</p>
      <p class="label__fragrance">Coconut Lime<br>soy candle</p>
    </div>
    <div class="label label--cream">
      <div class="label__paper" role="img" aria-label="Dark charcoal vintage damask paper background"></div>
      <div class="label__rule"></div>
      <p class="label__name">Velvet Hearth<br>Studio</p>
      <p class="label__fragrance">Coconut Lime<br>soy candle</p>
    </div>
    <div class="label label--rose">
      <div class="label__paper" role="img" aria-label="Dark charcoal vintage damask paper background"></div>
      <div class="label__rule"></div>
      <p class="label__name">Velvet Hearth<br>Studio</p>
      <p class="label__fragrance">Coconut Lime<br>soy candle</p>
    </div>
  </section>

  <div class="row-divider row-divider--first"></div>

  <section class="option-row option-row--round">
    <div class="label label--white">
      <div class="label__paper" role="img" aria-label="Dark charcoal vintage damask paper background"></div>
      <div class="label__rule"></div>
      <p class="label__name">Velvet Hearth<br>Studio</p>
      <p class="label__fragrance">Coconut Lime<br>soy candle</p>
    </div>
    <div class="label label--cream">
      <div class="label__paper" role="img" aria-label="Dark charcoal vintage damask paper background"></div>
      <div class="label__rule"></div>
      <p class="label__name">Velvet Hearth<br>Studio</p>
      <p class="label__fragrance">Coconut Lime<br>soy candle</p>
    </div>
    <div class="label label--rose">
      <div class="label__paper" role="img" aria-label="Dark charcoal vintage damask paper background"></div>
      <div class="label__rule"></div>
      <p class="label__name">Velvet Hearth<br>Studio</p>
      <p class="label__fragrance">Coconut Lime<br>soy candle</p>
    </div>
  </section>

  <div class="row-divider row-divider--second"></div>

  <section class="option-row option-row--formal">
    <div class="label label--white">
      <div class="label__paper" role="img" aria-label="Dark charcoal vintage damask paper background"></div>
      <div class="label__rule"></div>
      <p class="label__name">Velvet Hearth<br>Studio</p>
      <p class="label__fragrance">Coconut Lime<br>soy candle</p>
    </div>
    <div class="label label--cream">
      <div class="label__paper" role="img" aria-label="Dark charcoal vintage damask paper background"></div>
      <div class="label__rule"></div>
      <p class="label__name">Velvet Hearth<br>Studio</p>
      <p class="label__fragrance">Coconut Lime<br>soy candle</p>
    </div>
    <div class="label label--rose">
      <div class="label__paper" role="img" aria-label="Dark charcoal vintage damask paper background"></div>
      <div class="label__rule"></div>
      <p class="label__name">Velvet Hearth<br>Studio</p>
      <p class="label__fragrance">Coconut Lime<br>soy candle</p>
    </div>
  </section>

</main>
</body>
</html>
```